Zerovan Medical

We are a medical supplier company we sell machines and equipment to all medical sectors in Iraq. Our services include not only the installation of these machines and equipment but also we provide support after installation and we train the staff to use these machines/equipment
We need a website that will make us stand out from our competitors, something professional and catchy
Starting from the home page, before showing the home page we want the loading screen to have our logo animated in a nice way
Then we can proceed to creating the other pages which are
Projects
Services
Training
About
and Contact us
Attached below is our logo and the color blue that we hope to use in the theme of the website
**** In the home page we want to focus on our partners and services****

Target Market(s)

Medical Sector

Industry/Entity Type

Medical

Coding

Coded - Design and coding required

Number of Pages Required

5+ page

Colors
0054AA
0677BA
7BADD7
CADEEF
E8F1F8

Requirements
Must have
• Animation in loading screen or animation in home page
Nice to have
• Some sort of animation for our partners

```html
<!DOCTYPE html>
<html lang="en">
<head>
<meta charset="utf-8">
<title>Zerovan Medical — Medical Appliances</title>
<link href="https://fonts.googleapis.com/css2?family=Kanit:wght@400;500;600&family=Figtree:wght@400;500;600;700&display=swap" rel="stylesheet">
<style>
:root{
  --navy:#201f5c;
  --navy-deep:#141339;
  --navy-bar:#25246b;
  --blue:#1193d9;
  --blue-dark:#0054aa;
  --blue-soft:#7badd7;
  --blue-pale:#cadeef;
  --ink:#23234f;
  --text:#4a4a63;
  --grey-bg:#eef0f5;
  --white:#ffffff;
}
*{box-sizing:border-box;margin:0;padding:0}
html,body{width:1200px;height:5177px;overflow:hidden;background:var(--white)}
body{position:relative;font-family:"Figtree",sans-serif;color:var(--text)}
.abs{position:absolute}
.section{position:absolute;left:0;width:1200px;overflow:hidden}
h1,h2,h3,.heading{font-family:"Kanit",sans-serif;font-weight:600;color:var(--ink)}
.title{line-height:56px}
.eyebrow{font-family:"Figtree",sans-serif;font-size:14px;line-height:17px;font-weight:700;color:var(--blue);letter-spacing:.3px;text-transform:uppercase}
.btn{position:absolute;display:flex;align-items:center;justify-content:center;gap:6px;background:var(--blue);color:#fff;font-size:12px;font-weight:700;text-transform:uppercase;border-radius:2px;height:44px}
.photo{position:absolute;border-radius:18px}
.frame{position:absolute;border:3px solid #3aa0df;border-radius:24px}

/* header */
.site-header{top:0;height:92px;background:#fff}
.brand{position:absolute;display:flex;align-items:center;gap:12px;font-family:"Kanit",sans-serif;font-weight:600;font-size:30px;color:var(--blue-dark)}
.brand-square{width:30px;height:30px;background:var(--blue)}
.nav{position:absolute;top:0;left:0;width:1200px;height:92px}
.nav a{position:absolute;top:36px;font-size:14px;font-weight:600;color:var(--ink);text-decoration:none;text-transform:uppercase}
.nav a.active{color:var(--blue)}
.nav .cta{top:24px;left:968px;width:144px;height:44px;background:var(--blue);color:#fff;display:flex;align-items:center;justify-content:center;border-radius:3px;font-size:13px}

/* hero */
.hero{top:92px;height:566px}
.hero-photo{position:absolute;inset:0;background:linear-gradient(90deg,#3b3f4a 0%,#6f7480 35%,#b8c6d4 62%,#8fb0d6 80%,#c9d3de 100%)}
.hero-tag{position:absolute;left:166px;top:116px;background:var(--navy);color:#fff;font-size:19px;letter-spacing:6px;padding:0 12px;height:22px;line-height:22px;font-weight:500}
.hero h1{position:absolute;left:166px;color:#fff;line-height:1}
.hero-sub{position:absolute;left:166px;top:382px;font-size:29px;color:#fff}
.hero-arrow{position:absolute;top:252px;width:30px;height:60px}

/* about */
.about{top:658px;height:658px}
.about h2{position:absolute;left:614px;top:198px;width:520px;font-family:"Figtree",sans-serif;font-weight:400;font-size:24px;line-height:31px;color:var(--ink)}
.about p{position:absolute;left:614px;top:302px;width:490px;font-size:14px;line-height:24px}

/* services */
.services{top:1316px;height:658px;background:var(--navy)}
.services .title{position:absolute;left:86px;top:131px;font-size:46px;color:#fff}
.service-list{position:absolute;left:84px;top:230px;width:362px;height:282px;background:var(--navy-deep);border-radius:4px}
.service-item{position:absolute;left:0;width:362px;display:flex;align-items:center;gap:22px;padding-left:26px;color:#fff;font-size:18px;font-weight:600;line-height:24px}
.service-item.active{background:#2b9fdc;border-radius:4px 4px 0 0}
.service-item .icon{width:48px;height:48px;flex:none}
.service-detail h3{position:absolute;left:810px;top:190px;width:310px;font-size:31px;line-height:36px;color:#fff;font-weight:500}
.service-detail p{position:absolute;left:810px;top:316px;width:310px;font-size:15px;line-height:24px;color:#e7e9f5}

/* projects */
.projects{top:1974px;height:660px}
.center{position:absolute;left:0;width:1200px;text-align:center}
.projects .title{top:108px;font-size:46px}
.project-caption{position:absolute;top:526px;width:332px;text-align:center;font-size:18px;font-weight:700;color:var(--ink)}
.slider-btn{position:absolute;top:338px;width:36px;height:36px;border-radius:50%}

/* training */
.training{top:2634px;height:658px;background:var(--navy)}
.training .title{position:absolute;left:84px;top:108px;font-size:46px;color:#fff}
.training .lead{position:absolute;left:84px;top:176px;width:490px;font-size:15px;line-height:24px;color:#e7e9f5}
.checks{position:absolute;left:84px;top:270px;width:490px;list-style:none}
.checks li{position:relative;padding-left:30px;font-size:15px;line-height:22px;color:#fff;margin-bottom:22px}
.checks li svg{position:absolute;left:0;top:3px}

/* contact */
.contact{top:3292px;height:752px;background:var(--grey-bg)}
.contact .title{top:97px;font-size:46px}
.contact .lead{top:164px;font-size:15px;line-height:24px}
.contact-card{position:absolute;left:130px;top:234px;width:942px;height:458px;background:#fff;border-radius:4px}
.contact-info{position:absolute;left:8px;top:8px;width:404px;height:442px;background:var(--navy);border-radius:4px;overflow:hidden}
.contact-info h3{position:absolute;left:38px;top:44px;font-size:20px;color:#fff;font-weight:500}
.info-row{position:absolute;left:38px;display:flex;gap:14px;color:#fff;font-size:15px;line-height:22px}
.field{position:absolute;font-size:13px;font-weight:600;color:var(--ink)}
.field-line{position:absolute;height:1px;background:#b9bccb}

/* partners */
.partners{top:4044px;height:646px}
.partners .title{position:absolute;left:84px;top:346px;font-size:48px;line-height:54px}
.partners p{position:absolute;left:84px;top:470px;width:420px;font-size:15px;line-height:24px}
.badge{position:absolute;width:246px;height:110px;border:2px solid #cfd1d8;border-radius:10px;background:#f6f6f7;display:flex;align-items:center;justify-content:center}
.badge span{width:58px;height:58px;border-radius:50%;background:#8d8f96}

/* footer */
.footer{top:4690px;height:487px;background:var(--navy-deep)}
.footer h4{position:absolute;top:76px;font-size:14px;font-weight:700;letter-spacing:1.5px;color:#fff;text-transform:uppercase}
.footer ul{position:absolute;top:114px;list-style:none}
.footer li,.footer .about-text{font-size:14px;line-height:30px;color:#e2e3ee}
.footer .about-text{position:absolute;top:110px;left:84px;width:270px;line-height:24px}
.footer-bar{position:absolute;left:84px;top:344px;width:1030px;height:78px;background:var(--navy-bar)}
.social{position:absolute;top:30px;width:18px;height:18px;background:#fff;border-radius:3px}
.copyright{position:absolute;left:84px;top:456px;font-size:12px;letter-spacing:1px;color:#9c9dc0}
.copyright b{color:var(--blue)}
</style>
</head>
<body>

<header class="section site-header">
  <div class="brand" style="left:84px;top:26px"><span class="brand-square"></span>Zerovan Medical</div>
  <nav class="nav">
    <a class="active" style="left:500px">Home</a>
    <a style="left:578px">About</a>
    <a style="left:666px">Services</a>
    <a style="left:770px">Projects</a>
    <a style="left:878px">Training</a>
    <a class="cta" style="left:968px">Contact Us</a>
  </nav>
</header>

<section class="section hero">
  <div class="hero-photo" role="img" aria-label="Smiling medical technician in a white headscarf and blue uniform standing in a clean equipment room"></div>
  <div class="hero-tag">WE PROVIDE SUPPORT</div>
  <h1 style="top:150px;font-size:48px">After Installation</h1>
  <h1 style="top:210px;font-size:80px">And WeTrain</h1>
  <h1 style="top:294px;font-size:80px">The Staff</h1>
  <div class="hero-sub">To all medical sectors in Iraq</div>
  <div class="btn" style="left:166px;top:446px;width:166px">Discover More <svg width="12" height="10" viewBox="0 0 12 10"><path d="M0 5h10M6 1l4 4-4 4" stroke="#fff" stroke-width="1.6" fill="none"/></svg></div>
  <svg class="hero-arrow" style="left:84px" viewBox="0 0 30 60"><path d="M26 4L4 30l22 26" stroke="#fff" stroke-width="2" fill="none"/></svg>
  <svg class="hero-arrow" style="left:1086px" viewBox="0 0 30 60"><path d="M4 4l22 26L4 56" stroke="#fff" stroke-width="2" fill="none"/></svg>
</section>

<section class="section about">
  <div class="frame" style="left:84px;top:104px;width:472px;height:432px"></div>
  <div class="photo" style="left:98px;top:118px;width:444px;height:404px;background:linear-gradient(160deg,#e9eef3,#b9c6d2 60%,#dfe6ec)" role="img" aria-label="Anaesthesia workstation with monitor in a hospital room"></div>
  <div class="eyebrow abs" style="left:614px;top:174px">About Us</div>
  <h2>Curabitur diam lacus, dignissim at mattis nec, rhoncus sed ante. Nunc pu mauris, commodo at vulputate a, consequat vel ex.</h2>
  <p>Donec et quam tempor, consequat ex et, pulvinar velit. Vestibulum volutpat, augue eget porta malesuada, diam mi bibendum ante, id auctor magna tortor ut felis.</p>
  <div class="btn" style="left:614px;top:394px;width:158px">Read More <svg width="12" height="10" viewBox="0 0 12 10"><path d="M0 5h10M6 1l4 4-4 4" stroke="#fff" stroke-width="1.6" fill="none"/></svg></div>
</section>

<section class="section services">
  <div class="eyebrow abs" style="left:86px;top:108px">Services</div>
  <h2 class="title">What We Do</h2>
  <div class="service-list">
    <div class="service-item active" style="top:0;height:96px">
      <svg class="icon" viewBox="0 0 48 48"><circle cx="24" cy="24" r="15" stroke="#fff" stroke-width="2" fill="none"/><circle cx="24" cy="24" r="6" stroke="#fff" stroke-width="2" fill="none"/></svg>
      <span>Installation of these<br>machines and equipment</span>
    </div>
    <svg class="abs" style="left:362px;top:36px" width="12" height="24" viewBox="0 0 12 24"><path d="M0 0l12 12L0 24z" fill="#2b9fdc"/></svg>
    <div class="service-item" style="top:96px;height:86px">
      <svg class="icon" viewBox="0 0 48 48"><circle cx="24" cy="16" r="8" stroke="#fff" stroke-width="2" fill="none"/><path d="M10 42c0-9 6-14 14-14s14 5 14 14" stroke="#fff" stroke-width="2" fill="none"/></svg>
      <span>Support after installation</span>
    </div>
    <div class="abs" style="left:26px;top:182px;width:320px;border-top:1px dashed #5a5a8a"></div>
    <div class="service-item" style="top:182px;height:100px">
      <svg class="icon" viewBox="0 0 48 48"><rect x="22" y="6" width="22" height="14" stroke="#fff" stroke-width="2" fill="none"/><circle cx="10" cy="14" r="5" stroke="#fff" stroke-width="2" fill="none"/><circle cx="12" cy="34" r="5" stroke="#fff" stroke-width="2" fill="none"/><circle cx="32" cy="34" r="5" stroke="#fff" stroke-width="2" fill="none"/></svg>
      <span>We train the staff to use<br>these machines/equipment</span>
    </div>
  </div>
  <div class="frame" style="left:466px;top:168px;width:314px;height:378px"></div>
  <div class="photo" style="left:478px;top:180px;width:290px;height:354px;background:linear-gradient(170deg,#c9d6e2,#6d86a6 55%,#3d5a86)" role="img" aria-label="Surgical team working with medical equipment in an operating room"></div>
  <div class="service-detail">
    <h3>Installation of these machines and equipment</h3>
    <p>Lorem ipsum dolor sit amet, consectetur adipiscing elit, sed do eiuspor incididunt ut labore et dolore magna aliqua. Quis ipm susndisse ultrice. Risus commodo viverra maecenas accumsan lacus vel facilisis.</p>
  </div>
  <div class="btn" style="left:810px;top:466px;width:148px">Read More <svg width="12" height="10" viewBox="0 0 12 10"><path d="M0 5h10M6 1l4 4-4 4" stroke="#fff" stroke-width="1.6" fill="none"/></svg></div>
</section>

<section class="section projects">
  <div class="eyebrow center" style="top:88px">Projects</div>
  <h2 class="center title">Our Latest Projects</h2>
  <div class="frame" style="left:92px;top:188px;width:332px;height:320px;border-radius:0 0 22px 0"></div>
  <div class="photo" style="left:102px;top:198px;width:312px;height:300px;border-radius:0 0 16px 0;background:linear-gradient(160deg,#d7dde3,#8fa9ad 50%,#4f9a92)" role="img" aria-label="Technician in protective clothing operating a production machine"></div>
  <div class="frame" style="left:434px;top:188px;width:332px;height:320px;border-radius:0 0 22px 0"></div>
  <div class="photo" style="left:444px;top:198px;width:312px;height:300px;border-radius:0 0 16px 0;background:linear-gradient(160deg,#e4e8ec,#a9b9c6 50%,#7aa4b8)" role="img" aria-label="Technicians in cleanroom suits inspecting stainless steel equipment"></div>
  <div class="frame" style="left:782px;top:188px;width:332px;height:320px;border-radius:0 0 22px 0"></div>
  <div class="photo" style="left:792px;top:198px;width:312px;height:300px;border-radius:0 0 16px 0;background:linear-gradient(160deg,#dfe5ea,#3a8fc8 55%,#8aa5bd)" role="img" aria-label="Engineer working at a blue laboratory machine"></div>
  <div class="project-caption" style="left:92px">Praesent quam mattis sit</div>
  <div class="project-caption" style="left:434px">Praesent quam mattis sit</div>
  <div class="project-caption" style="left:782px">Praesent quam mattis sit</div>
  <svg class="slider-btn" style="left:74px" viewBox="0 0 36 36"><circle cx="18" cy="18" r="18" fill="#201f5c"/><path d="M21 11l-7 7 7 7" stroke="#fff" stroke-width="2" fill="none"/></svg>
  <svg class="slider-btn" style="left:1094px" viewBox="0 0 36 36"><circle cx="18" cy="18" r="18" fill="#2b9fdc"/><path d="M15 11l7 7-7 7" stroke="#fff" stroke-width="2" fill="none"/></svg>
</section>

<section class="section training">
  <h2 class="title">Our Training</h2>
  <p class="lead">Morbi euismod malesuada nulla vel sagittis. Aliquam ut velit nulla. Ut a arcu sit amet magna pretium luctus. Aliquam id lacinia tellus. Ut nec risus tempus, pulvinar lectus quis, mattis mauris</p>
  <ul class="checks">
    <li><svg width="16" height="16" viewBox="0 0 16 16"><circle cx="8" cy="8" r="8" fill="#2b9fdc"/><path d="M4.5 8l2.5 2.5 4.5-5" stroke="#fff" stroke-width="1.6" fill="none"/></svg>Suspendisse facilisis commodo ligula, nosis nibh vulputate ac.</li>
    <li><svg width="16" height="16" viewBox="0 0 16 16"><circle cx="8" cy="8" r="8" fill="#2b9fdc"/><path d="M4.5 8l2.5 2.5 4.5-5" stroke="#fff" stroke-width="1.6" fill="none"/></svg>Class aptent taciti sociosqu ad litora torquent per conubia nostra.</li>
    <li><svg width="16" height="16" viewBox="0 0 16 16"><circle cx="8" cy="8" r="8" fill="#2b9fdc"/><path d="M4.5 8l2.5 2.5 4.5-5" stroke="#fff" stroke-width="1.6" fill="none"/></svg>Phasellus lobortis commodo mollis. Quisque quis finibus ligula.</li>
    <li><svg width="16" height="16" viewBox="0 0 16 16"><circle cx="8" cy="8" r="8" fill="#2b9fdc"/><path d="M4.5 8l2.5 2.5 4.5-5" stroke="#fff" stroke-width="1.6" fill="none"/></svg>Vivamus nec velit non risus accumsan egestas.</li>
  </ul>
  <div class="btn" style="left:84px;top:470px;width:148px">Read More <svg width="12" height="10" viewBox="0 0 12 10"><path d="M0 5h10M6 1l4 4-4 4" stroke="#fff" stroke-width="1.6" fill="none"/></svg></div>
  <div class="frame" style="left:644px;top:112px;width:470px;height:430px"></div>
  <div class="photo" style="left:658px;top:126px;width:442px;height:402px;background:linear-gradient(160deg,#dde4ea,#9fb3c2 45%,#3fb5a8)" role="img" aria-label="Trainee in teal scrubs and hairnet operating an industrial control panel"></div>
</section>

<section class="section contact">
  <div class="eyebrow center" style="top:76px">Contact Us</div>
  <h2 class="center title">Get In Touch</h2>
  <p class="center lead">Praesent quam mi, mattis sit amet nisl in, aliquet tempor lectus. In dapis lacinia libero sit amet sodales.<br>Nulla elementum magna nec placerat sollicitudin</p>
  <div class="contact-card">
    <div class="contact-info">
      <h3>Contact Information</h3>
      <div class="info-row" style="top:86px"><svg width="12" height="16" viewBox="0 0 12 16"><path d="M6 0a6 6 0 016 6c0 4-6 10-6 10S0 10 0 6a6 6 0 016-6z" fill="#2b9fdc"/><circle cx="6" cy="6" r="2" fill="#201f5c"/></svg><span>12 Cedar Lane, Babylon Block<br>Karbala, Iraq</span></div>
      <div class="info-row" style="top:150px"><svg width="14" height="14" viewBox="0 0 14 14"><path d="M3 0l3 3-2 2c1 2 3 4 5 5l2-2 3 3-2 3C6 14 0 8 0 3z" fill="#2b9fdc"/></svg><span>1800-555-019</span></div>
      <div class="info-row" style="top:192px"><svg width="14" height="12" viewBox="0 0 14 12"><rect width="14" height="12" rx="1" fill="#2b9fdc"/><path d="M1 2l6 4 6-4" stroke="#201f5c" stroke-width="1.4" fill="none"/></svg><span>info@zerovanmedical.com</span></div>
      <div class="abs" style="left:120px;top:236px;width:284px;height:206px;background:linear-gradient(150deg,#dbe6ef,#6f97c2 55%,#2b6fb6)" role="img" aria-label="Surgeon in blue scrubs at an operating table"></div>
    </div>
    <div class="field" style="left:442px;top:52px">First name</div>
    <div class="field-line" style="left:442px;top:96px;width:228px"></div>
    <div class="field" style="left:690px;top:52px">Last Name</div>
    <div class="field-line" style="left:690px;top:96px;width:222px"></div>
    <div class="field" style="left:442px;top:120px">Email</div>
    <div class="field-line" style="left:442px;top:164px;width:228px"></div>
    <div class="field" style="left:690px;top:120px">Phone</div>
    <div class="field-line" style="left:690px;top:164px;width:222px"></div>
    <div class="field" style="left:442px;top:216px">Message</div>
    <div class="field-line" style="left:442px;top:316px;width:470px"></div>
    <div class="btn" style="left:440px;top:342px;width:128px;height:40px">Submit <svg width="12" height="10" viewBox="0 0 12 10"><path d="M0 5h10M6 1l4 4-4 4" stroke="#fff" stroke-width="1.6" fill="none"/></svg></div>
  </div>
</section>

<section class="section partners">
  <h2 class="title">Our High-level<br>Partners</h2>
  <p>Donec et quam tempor, consequat ex et, pulvinar velit. Vestibulum volutpat, augue eget porta malesuada, diam mi bibendum ante, id auctor magna to</p>
  <div class="badge" style="left:604px;top:76px"><span></span></div>
  <div class="badge" style="left:868px;top:76px"><span></span></div>
  <div class="badge" style="left:604px;top:204px"><span></span></div>
  <div class="badge" style="left:868px;top:204px"><span></span></div>
  <div class="badge" style="left:604px;top:332px"><span></span></div>
  <div class="badge" style="left:868px;top:332px"><span></span></div>
  <div class="badge" style="left:604px;top:460px"><span></span></div>
  <div class="badge" style="left:868px;top:460px"><span></span></div>
</section>

<footer class="section footer">
  <h4 style="left:84px">About Us</h4>
  <p class="about-text">Integer mi nisi, congid turpis ac, ultricies tempor est. Quisque vel eros posuere, hendrerit ipsum in, finurna. Pellentesque feugiat id elit vel sollicitudin.</p>
  <h4 style="left:440px">Quick Links</h4>
  <ul style="left:440px"><li>Home</li><li>About</li><li>Services</li><li>Projects</li><li>Training</li><li>Contact Us</li></ul>
  <h4 style="left:662px">Services</h4>
  <ul style="left:662px;width:320px"><li>Installation of these machines and equipment</li><li>Support after installation</li><li style="line-height:22px;margin-top:4px">We train the staff to use these<br>machines/equipment</li></ul>
  <h4 style="left:1038px">Training</h4>
  <ul style="left:1038px"><li>Training 01</li><li>Training 02</li><li>Training 03</li><li>Training 04</li><li>Training 05</li></ul>
  <div class="footer-bar">
    <div class="brand" style="left:22px;top:20px;color:#fff"><span class="brand-square"></span>Zerovan Medical</div>
    <span class="social" style="left:900px"></span>
    <span class="social" style="left:930px"></span>
    <span class="social" style="left:960px"></span>
    <span class="social" style="left:990px"></span>
  </div>
  <div class="copyright">© 2024 <b>ZEROVAN MEDICAL</b>. ALL RIGHT RESERVED</div>
</footer>

</body>
</html>
```